Business Card Design for Oncology Consulting Company

We need a business card design using a logo that has already been created.

Company name is: ORBVA - Guild for Lumora Mapping, Welfare and Outreach

We would also like to include the following pieces of information on the business card:
Name
Title
US Address (street, city, state, zip, country)
Email address
Website address

Target Market(s)

The target customers are physicians (oncologists, pathologists) in Greece, Iran, US, etc who would refer patients to our company for a second medical opinion/genetic counseling for cancer.

Industry/Entity Type

Business

Colors

Designer to choose colors to be used in the design.

Requirements
Must have
• Must contain logo in attached file and elements described above.

```html
<!DOCTYPE html>
<html lang="en">
<head>
<meta charset="utf-8">
<title>ORBVA Business Card</title>
<link rel="stylesheet" href="https://fonts.googleapis.com/css2?family=Montserrat:wght@300;400;600&family=Archivo+Black&display=swap">
<style>
  :root {
    --bg: #2a2a2a;
    --card-white: #ffffff;
    --card-black: #0b0b0b;
    --band-dark: #1b1b1b;
    --brand-blue: #1466b0;
    --ink: #111111;
    --muted: #8a8a8a;
    --tile-grey: #d6d6d6;
    --web-grey: #c9c9c9;
  }
  * { margin: 0; padding: 0; box-sizing: border-box; }
  html, body { width: 1200px; height: 900px; overflow: hidden; }
  body {
    background: var(--bg);
    font-family: "Montserrat", Arial, sans-serif;
    position: relative;
  }
  .card {
    position: absolute;
    left: 250px;
    width: 700px;
    height: 400px;
    overflow: hidden;
    box-shadow: 0 10px 30px rgba(0,0,0,0.5);
  }

  /* Back side */
  .card-back { top: 35px; background: var(--card-black); }
  .back-band {
    position: absolute; left: 0; top: 130px; width: 700px; height: 110px;
    background: var(--band-dark);
  }
  .end-tile {
    position: absolute; top: 150px; width: 60px; height: 70px;
    background: linear-gradient(135deg, #e6e6e6, var(--tile-grey));
  }
  .end-tile.left { left: 0; }
  .end-tile.right { right: 0; }
  .back-logo {
    position: absolute; left: 90px; top: 150px;
    display: flex; flex-direction: column;
  }
  .back-logo .wordmark {
    font-weight: 600; font-size: 58px; letter-spacing: 3px;
    color: var(--brand-blue); line-height: 1;
  }
  .back-logo .tagline {
    margin-top: 6px; font-size: 8px; letter-spacing: 1px;
    color: var(--muted); text-transform: uppercase; white-space: nowrap;
    border-top: 1px solid var(--muted); padding-top: 3px;
  }
  .back-web {
    position: absolute; left: 300px; top: 262px;
    font-size: 26px; font-weight: 300; letter-spacing: 1px;
    color: var(--web-grey);
  }

  /* Front side */
  .card-front { top: 465px; background: var(--card-white); }
  .front-shapes { position: absolute; inset: 0; }
  .front-logo {
    position: absolute; left: 318px; top: 58px;
    display: flex; align-items: flex-end; gap: 8px;
  }
  .front-logo .wordmark {
    font-weight: 600; font-size: 40px; letter-spacing: 2px;
    color: var(--brand-blue); line-height: 1;
  }
  .front-logo .tagline {
    font-size: 6px; letter-spacing: 0.4px; color: var(--muted);
    text-transform: uppercase; white-space: nowrap;
    border-top: 1px solid var(--muted);
    padding-top: 2px; margin-bottom: 4px;
  }
  .holder {
    position: absolute; left: 80px; top: 125px;
  }
  .holder .name {
    font-weight: 300; font-size: 27px; letter-spacing: 3px; color: var(--ink);
  }
  .holder .name .accent { color: var(--brand-blue); font-weight: 400; }
  .holder .title {
    font-size: 17px; letter-spacing: 2px; color: var(--brand-blue); margin-top: 2px;
  }
  .contact {
    position: absolute; left: 80px; top: 258px;
    list-style: none;
    font-family: "Archivo Black", Arial, sans-serif;
    font-size: 17px; letter-spacing: 1px; color: var(--ink); line-height: 1.3;
  }
</style>
</head>
<body>

  <section class="card card-back" aria-label="Card back">
    <div class="back-band"></div>
    <div class="end-tile left" role="img" aria-label="Decorative end tile"></div>
    <div class="back-logo">
      <span class="wordmark">ORBVA</span>
      <span class="tagline">Guild for Lumora Mapping, Welfare and Outreach</span>
    </div>
    <div class="end-tile right" role="img" aria-label="Decorative end tile"></div>
    <p class="back-web">yourwebsite.com</p>
  </section>

  <section class="card card-front" aria-label="Card front">
    <svg class="front-shapes" viewBox="0 0 700 400" aria-hidden="true">
      <rect x="0" y="155" width="45" height="40" fill="var(--card-black)"/>
      <polygon points="52,155 78,155 62,195 36,195" fill="var(--brand-blue)"/>
      <rect x="0" y="372" width="700" height="28" fill="var(--card-black)"/>
      <polygon points="440,372 540,372 560,335 460,335" fill="var(--brand-blue)"/>
      <polygon points="420,372 440,372 460,335 440,335" fill="var(--card-black)"/>
    </svg>
    <div class="front-logo">
      <span class="wordmark">ORBVA</span>
      <span class="tagline">Guild for Lumora Mapping, Welfare and Outreach</span>
    </div>
    <div class="holder">
      <p class="name">Your <span class="accent">Name</span></p>
      <p class="title">Title</p>
    </div>
    <ul class="contact">
      <li>Address: street, city, state, zip, country</li>
      <li>E-Mail: email@xyz</li>
      <li>Contact: 000-000-0000</li>
      <li>Web: yoururl</li>
    </ul>
  </section>

</body>
</html>
```